The Willow Nest

a business card that we will give to customers, Doctors, Midwifes, surgeons, Pilates and Yoga instructors, chiropractors, physiotherapists.
Our business is based in Australia, Melbourne

Please visit our website to get a better idea about our business www.thewillownest.com.au
Updates

Target Market(s)

health, wellbeing, no surgery, natural healing, medical

Industry/Entity Type

Business

Contact Information for Business Card

Mira Holcott
Pilates Instructor
0412 608 271

Rosalind Garrick
Yoga Instructor
0409 375 516

email thewillownest@quillmail.com
Website www.thewillownest.com.au

Requirements
Must have
• A classy, sophisticated feel.

front and back
Use of our business Logo (either in black or white)
Use of Varenko Method Logo - this logo must be smaller then our business logo as it is just a contractual legal requirement to have this logo

NOTE: we could not upload more files as this would only let us upload one file - please contact us for the other logo's.
Nice to have
• targeted at both female and male.

Different base colours on each side

our business is about repairing separated abdominals:
Do you have a Bulging belly?
Do you get asked if you are pregnant?
Have been diagnosed with a Diastasis Recti?
Do you Suffer back pain or hip pain?
Weak core strength and weak pelvic floor?
Considering a tummy tuck? (it can be healed without surgery)
Have an umbilical hernia?
An "Outie" belly button that used to be an "Innie"?
Plus we specialise in Pilates and yoga

```html
<!DOCTYPE html>
<html lang="en">
<head>
<meta charset="utf-8">
<title>The Willow Nest — Business Card</title>
<link href="https://fonts.googleapis.com/css2?family=Questrial&display=swap" rel="stylesheet">
<style>
  :root {
    --page-bg: #e6e8ea;
    --card-front: #ffffff;
    --card-back: #2b2b2c;
    --brand-blue: #1e6a9e;
    --accent-blue: #2a8fd0;
    --accent-red: #ef4a2e;
    --text-grey: #6d6f72;
    --rule-blue: #2f6f9c;
    --back-text: #f2f2f2;
    --back-sub: #a8a8aa;
  }
  * { box-sizing: border-box; margin: 0; padding: 0; }
  html, body {
    width: 1200px;
    height: 960px;
    overflow: hidden;
    background: var(--page-bg);
    font-family: "Questrial", "Century Gothic", sans-serif;
  }
  .canvas {
    position: relative;
    width: 1200px;
    height: 960px;
  }
  .card {
    position: absolute;
    left: 320px;
    width: 560px;
    height: 342px;
    box-shadow: 0 10px 28px rgba(0,0,0,0.18);
  }
  .card--front { top: 110px; background: var(--card-front); }
  .card--back  { top: 508px; background: var(--card-back); }

  /* Front */
  .brand {
    position: absolute;
    left: 30px;
    top: 32px;
    display: flex;
    align-items: center;
    gap: 12px;
  }
  .brand__dot {
    width: 34px;
    height: 34px;
    border-radius: 50%;
    border: 3px solid var(--accent-blue);
  }
  .brand__name {
    font-size: 34px;
    color: var(--brand-blue);
    letter-spacing: 0.2px;
  }
  .brand__tagline {
    position: absolute;
    left: 124px;
    top: 80px;
    font-size: 11px;
    letter-spacing: 1px;
    color: var(--text-grey);
  }
  .team {
    position: absolute;
    left: 30px;
    top: 196px;
  }
  .team__row {
    display: flex;
    align-items: baseline;
    gap: 8px;
    margin-bottom: 10px;
  }
  .team__name { font-size: 23px; color: var(--brand-blue); }
  .team__sep  { font-size: 18px; color: var(--text-grey); }
  .team__role { font-size: 16px; color: var(--text-grey); }
  .team__role--caps { letter-spacing: 0.5px; }

  .phones {
    position: absolute;
    right: 28px;
    top: 186px;
  }
  .phones__row {
    display: flex;
    align-items: center;
    gap: 12px;
    font-size: 15px;
    color: var(--text-grey);
    margin-bottom: 16px;
  }
  .icon { width: 14px; height: 16px; flex: none; }

  .website {
    position: absolute;
    right: 28px;
    top: 264px;
    display: flex;
    align-items: center;
    gap: 8px;
    font-size: 14px;
    color: var(--text-grey);
    font-weight: 400;
  }
  .rule {
    position: absolute;
    left: 30px;
    right: 28px;
    top: 288px;
    height: 1px;
    background: var(--rule-blue);
  }
  .email {
    position: absolute;
    left: 30px;
    top: 302px;
    display: flex;
    align-items: center;
    gap: 10px;
    font-size: 17px;
    color: var(--text-grey);
  }

  /* Back */
  .back-brand {
    position: absolute;
    left: 0;
    right: 0;
    top: 118px;
    display: flex;
    justify-content: center;
    align-items: center;
    gap: 14px;
  }
  .back-brand__dot {
    width: 26px;
    height: 26px;
    border-radius: 50%;
    background: var(--accent-red);
  }
  .back-brand__name {
    font-size: 36px;
    color: var(--back-text);
  }
  .partner {
    position: absolute;
    left: 0;
    right: 0;
    top: 262px;
    text-align: center;
    font-size: 13px;
    letter-spacing: 0.4px;
    color: var(--back-text);
  }
</style>
</head>
<body>
<main class="canvas">

  <section class="card card--front" aria-label="Business card front">
    <div class="brand">
      <span class="brand__dot"></span>
      <span class="brand__name">The Willow Nest</span>
    </div>
    <p class="brand__tagline">ABDOMINAL REHABILITATION</p>

    <div class="team">
      <p class="team__row">
        <span class="team__name">Mira Holcott</span>
        <span class="team__sep">|</span>
        <span class="team__role team__role--caps">PILATES INSTRUCTOR</span>
      </p>
      <p class="team__row">
        <span class="team__name">Rosalind Garrick</span>
        <span class="team__sep">|</span>
        <span class="team__role">Yoga Instructor</span>
      </p>
    </div>

    <div class="phones">
      <p class="phones__row">
        <svg class="icon" viewBox="0 0 14 16" aria-hidden="true"><rect x="3" y="0.5" width="8" height="15" rx="1.5" fill="none" stroke="#1e6a9e" stroke-width="1.4"/><rect x="4.6" y="2.5" width="4.8" height="5" fill="#1e6a9e"/><circle cx="7" cy="12.5" r="1" fill="#1e6a9e"/></svg>
        0412 608 271
      </p>
      <p class="phones__row">
        <svg class="icon" viewBox="0 0 14 16" aria-hidden="true"><rect x="3" y="0.5" width="8" height="15" rx="1.5" fill="none" stroke="#1e6a9e" stroke-width="1.4"/><rect x="4.6" y="2.5" width="4.8" height="5" fill="#1e6a9e"/><circle cx="7" cy="12.5" r="1" fill="#1e6a9e"/></svg>
        0409 375 516
      </p>
    </div>

    <p class="website">
      <svg class="icon" viewBox="0 0 16 16" aria-hidden="true"><circle cx="8" cy="8" r="7" fill="#1e6a9e"/><path d="M1 8h14M8 1c-3 3.5-3 10.5 0 14M8 1c3 3.5 3 10.5 0 14" stroke="#fff" stroke-width="1" fill="none"/></svg>
      www.thewillownest.com.au
    </p>
    <div class="rule"></div>
    <p class="email">
      <svg class="icon" viewBox="0 0 18 14" style="width:18px;height:14px" aria-hidden="true"><rect x="1" y="1" width="16" height="12" fill="none" stroke="#1e6a9e" stroke-width="1.5"/><path d="M1 1l8 7 8-7M1 13l6-5.5M17 13l-6-5.5" fill="none" stroke="#1e6a9e" stroke-width="1.3"/></svg>
      thewillownest@quillmail.com
    </p>
  </section>

  <section class="card card--back" aria-label="Business card back">
    <div class="back-brand">
      <span class="back-brand__dot"></span>
      <span class="back-brand__name">The Willow Nest</span>
    </div>
    <p class="partner">Varenko Method</p>
  </section>

</main>
</body>
</html>
```